Business Card Design Project for Electrical Company

We need a business card designed for a new Electrical Company called Venrol Electrical Solutions, i dont mind if only Venrol Electrical is used. We are a domestic and commercial Electrical Company that provides a range of Electrical Services. Our Company colours are Fluro Yellow and Black with the Lightning bolt picture attached.I have attached a card that has been made i think it is rather basic and am looking for something more. the font of Venrol Electrical has been used on our car graphics as well as the lightning bolt. i want to keep them the same so we can brand our business. Some things we want on the front of the card are Venrol Electrical Solutions, Derek Pollard, 0438562917, admin@venrolelectrical.example, Lic No 58342, Servicing CQ Region. But we want Dereks name seperate to the phone number as its the phone number for the office, derek wont be answering the phone so we are thinking we dont want to give that impression. What do you think? with all that if you have complete different font designs please submit what you think would work best. keeping in mind our company name and details as well as coulors.

Industry/Entity Type

Business

```html
<!DOCTYPE html>
<html lang="en">
<head>
<meta charset="utf-8">
<title>Venrol Electrical – Business Card</title>
<link rel="stylesheet" href="https://fonts.googleapis.com/css2?family=Questrial&family=Roboto+Condensed:wght@300&display=swap">
<style>
  :root {
    --backdrop: #3a3a3a;
    --card-base: #151515;
    --card-glow: #333333;
    --card-edge: #0e0e0e;
    --band: #0a0a0a;
    --brand-yellow: #e4f21a;
    --text-light: #b9b9b9;
    --text-mid: #9a9a9a;
    --divider: #4a4a4a;
  }
  * { box-sizing: border-box; margin: 0; padding: 0; }
  html, body {
    width: 1200px; height: 1000px; overflow: hidden;
    background: var(--backdrop);
  }
  .stage { position: relative; width: 1200px; height: 1000px; }
  .card {
    position: absolute; left: 275px; width: 664px;
    background: radial-gradient(ellipse at 50% 30%, var(--card-glow) 0%, var(--card-base) 55%, var(--card-edge) 100%);
    overflow: hidden;
    font-family: "Questrial", "Century Gothic", sans-serif;
    box-shadow: 0 2px 8px rgba(0,0,0,.45);
  }
  .card--front { top: 115px; height: 382px; }
  .card--back { top: 537px; height: 378px; }

  .holder { position: absolute; right: 339px; top: 172px; text-align: right; }
  .holder__name {
    font-family: "Roboto Condensed", "Arial Narrow", sans-serif;
    font-weight: 300; font-size: 32px; letter-spacing: -1px;
    color: var(--text-light); line-height: 1;
  }
  .holder__role {
    font-size: 9.5px; letter-spacing: .5px; color: var(--text-mid);
    text-transform: uppercase; margin-top: 3px;
  }
  .divider {
    position: absolute; left: 357px; top: 125px; width: 1px; height: 240px;
    background: linear-gradient(to bottom, transparent, var(--divider) 40%, var(--divider) 60%, transparent);
  }
  .brand {
    position: absolute; left: 370px; top: 152px;
    color: var(--brand-yellow); font-size: 40px; line-height: 1;
    text-transform: uppercase; letter-spacing: .5px;
  }
  .contact { position: absolute; left: 452px; top: 271px; font-size: 11px; color: var(--text-light); line-height: 1.25; letter-spacing: .4px; }
  .contact__region { margin-bottom: 15px; }
  .email { position: absolute; right: 26px; top: 340px; font-size: 13px; color: var(--text-light); letter-spacing: .4px; }
  .licence { position: absolute; left: 36px; top: 334px; font-size: 14.5px; color: var(--text-mid); letter-spacing: .5px; }

  .services {
    position: absolute; left: 50px; top: 66px;
    display: grid; grid-template-columns: 275px 275px; row-gap: 31px;
    list-style: none; font-size: 25px; letter-spacing: .8px; color: var(--text-mid); line-height: 33px;
  }
  .services li::before { content: "- "; }
  .tagline {
    position: absolute; left: 0; bottom: 0; width: 100%; height: 47px;
    background: var(--band); color: var(--text-light);
    font-size: 23px; letter-spacing: 1.5px; text-align: center; line-height: 47px;
  }
</style>
</head>
<body>
<main class="stage">
  <section class="card card--front" aria-label="Card front">
    <div class="holder">
      <p class="holder__name">Derek Pollard</p>
      <p class="holder__role">Licensed Electrician</p>
    </div>
    <div class="divider"></div>
    <h1 class="brand">Venrol<br>Electrical</h1>
    <div class="contact">
      <p class="contact__region">Servicing CQ Region</p>
      <p>Phone office:</p>
      <p>0438562917</p>
    </div>
    <p class="email">admin@venrolelectrical.example</p>
    <p class="licence">Lic No. 58342</p>
  </section>

  <section class="card card--back" aria-label="Card back">
    <ul class="services">
      <li>Light &amp; Power</li>
      <li>Renovations</li>
      <li>TV &amp; DATA</li>
      <li>Design &amp; Installation</li>
      <li>Test &amp; Tagging</li>
      <li>Air Con Installation</li>
      <li>Residential</li>
      <li>Smoke Detectors</li>
    </ul>
    <p class="tagline">LIGHTING UP CQ</p>
  </section>
</main>
</body>
</html>
```